Poster Design Project - Maple Bar and Restaurant

We require a Horse Racing Carnival poster (Northgate Autumn Turf Festival) to showcase the offer at our Bar/Restaurant.

The venue is called MAPLE. Our website is www.maplelounge.example.au

The venue is heavily design focused with significant use of strong graphics and logos.

The poster will need to be printed out in AO size.
Updates

Once again, thank you all for participating in this design creation. We are going to list a number of other poster briefs shortly that will require strong quirky/design graphics. I hope you'll all participate.

I am happy to provide individual responses to queries about specific designs and why they have been unsuccessful.

Overall we were really impressed with the quality of the submissions.

Thanks Gareth

Target Market(s)

Our demographic is 25-35 years old

Industry/Entity Type

Restaurant

Requirements
Must have
• The following copy needs to be incorporated into the poster -

MAPLE

AUTUMN TURF FESTIVAL 2011

Harrow Day - 29th October 2011
Champagne breakfast from 9am
Buses to and from the track
$15 bus ticket includes redeemable drink voucher
DJ from 8pm until 3am

Kestrel Plate Eve - 31st October 2011
Drink specials all night
DJ from 8pm until close

Kestrel Plate Day - 1st November 2011
Big screen racing live on 3 screens
Cocktail and drinks specials all day
DJ from 4pm

Willows Day - 3rd November 2011
DJ from 8pm until close

Lantern Day - 5th November 2011
The finishing post - Complimentary glass of sparkling with presentation of race entry ticket
DJ's from 9pm until 3am

For further enquiries and to secure your bus tickets please contact Orla on 95184726.

118 Pemberton Street, West Fairhaven Vic 3917
Tel: 95184726
Twitter: @themaplelounge
Facebook: Maple Bar and Restaurant
www.maplelounge.example.au
Should not have
• No cheesy graphics

```html
<!DOCTYPE html>
<html lang="en">
<head>
<meta charset="utf-8">
<title>Maple – Autumn Turf Festival 2011</title>
<link rel="stylesheet" href="https://fonts.googleapis.com/css2?family=Sancreek&family=Oswald:wght@300;400;600&family=Lobster+Two:ital,wght@1,700&display=swap">
<style>
  :root {
    --page: #dcd8d1;
    --teal: #4f8a80;
    --teal-deep: #3f7469;
    --ink: #233f3e;
    --cream: #f1ebe0;
    --lime: #a8bb3f;
    --rule: #6f7f7a;
    --display: "Sancreek", "Oswald", sans-serif;
  }
  * { box-sizing: border-box; margin: 0; padding: 0; }
  html, body { width: 993px; height: 1200px; overflow: hidden; background: var(--page); }
  .poster {
    position: absolute; left: 95px; top: 36px; width: 802px; height: 1128px;
    background: var(--teal); overflow: hidden;
  }
  .hero-art {
    position: absolute; left: 205px; top: 30px; width: 360px; height: 175px;
    background: linear-gradient(180deg, var(--teal-deep) 0%, #3a6b62 100%);
    border-radius: 46% 54% 0 0 / 60% 60% 0 0;
  }
  .header {
    position: absolute; left: 55px; top: 200px; width: 689px; height: 241px;
    background: var(--ink); overflow: hidden;
  }
  .the-badge {
    position: absolute; left: 366px; top: 168px; width: 68px; height: 46px;
    background: var(--ink); border: 2px solid var(--lime); border-radius: 10px;
    color: var(--lime); font: 24px/42px var(--display); text-align: center;
    z-index: 2;
  }
  .title {
    position: absolute; left: 0; width: 100%; text-align: center; white-space: nowrap;
    color: var(--cream); font-family: var(--display); font-weight: 400;
    font-size: 80px; line-height: 1; letter-spacing: 1px;
  }
  .title--top { top: 36px; }
  .title--bottom { top: 134px; }
  .title .star { color: var(--lime); font-size: 34px; vertical-align: middle; margin: 0 14px; }
  .flourish {
    position: absolute; top: 172px; width: 40px; height: 12px;
    background: var(--lime); border-radius: 6px;
  }
  .flourish--left { left: 70px; }
  .flourish--right { right: 70px; }

  .schedule {
    position: absolute; left: 55px; top: 441px; width: 689px; height: 518px;
    background: var(--cream);
  }
  .event { position: absolute; left: 0; width: 100%; height: 102px; }
  .event + .event::before {
    content: ""; position: absolute; left: 31px; right: 28px; top: -2px; height: 4px;
    border-top: 1px solid var(--rule); border-bottom: 1px solid var(--rule);
  }
  .event-name {
    position: absolute; left: 31px; top: 26px; width: 115px; height: 50px;
    background: var(--ink); outline: 1px solid var(--ink); outline-offset: 2px;
    border: 1px solid var(--cream);
    display: flex; align-items: center; justify-content: center; text-align: center;
    color: var(--lime); font: 600 13px/1.05 "Oswald", sans-serif; letter-spacing: 1px;
    text-transform: uppercase;
  }
  .event-date {
    position: absolute; left: 184px; width: 120px; top: 50%; transform: translateY(-50%);
    text-align: center; color: var(--ink);
    font: italic 700 18px/1.05 "Lobster Two", serif;
  }
  .event-details {
    position: absolute; left: 339px; width: 330px; top: 50%; transform: translateY(-50%);
    color: #4a5553; font: 300 14px/21px "Oswald", sans-serif; list-style: none;
  }

  .contact-band {
    position: absolute; left: 55px; top: 959px; width: 689px; height: 49px;
    background: var(--ink); color: var(--cream);
    font: 400 12.5px/49px "Oswald", sans-serif; letter-spacing: 1.2px; text-align: center;
    white-space: nowrap;
  }
  .contact-band .tick {
    display: inline-block; width: 20px; height: 5px; border-radius: 3px;
    background: var(--lime); vertical-align: middle; margin: 0 14px;
  }

  .footer { position: absolute; left: 0; top: 1033px; width: 100%; height: 60px; color: #2d5651; }
  .brand {
    position: absolute; left: 134px; top: 14px;
    font: 600 28px/1 "Oswald", sans-serif; letter-spacing: 4px; color: var(--ink);
  }
  .divider { position: absolute; top: 0; width: 1px; height: 60px; background: #2d5651; opacity: .7; }
  .divider--one { left: 272px; }
  .divider--two { left: 466px; }
  .address, .social { position: absolute; top: 0; list-style: none;
    font: 300 12.5px/22px "Oswald", sans-serif; letter-spacing: 1.4px; text-transform: uppercase; }
  .address { left: 294px; }
  .social { left: 494px; }
  .social li { display: flex; align-items: center; gap: 18px; }
  .social .dot { width: 8px; height: 8px; border-radius: 50%; background: #2d5651; }
</style>
</head>
<body>
<main class="poster">
  <div class="hero-art" role="img" aria-label="Silhouette of a jockey riding a racehorse"></div>

  <header class="header">
    <h1>
      <span class="title title--top">AUTUMN<span class="star">★</span>TURF</span>
      <span class="title title--bottom">FESTIVAL</span>
    </h1>
    <span class="flourish flourish--left" role="img" aria-label="Decorative flourish"></span>
    <span class="flourish flourish--right" role="img" aria-label="Decorative flourish"></span>
  </header>
  <div class="the-badge">THE</div>

  <section class="schedule">
    <article class="event" style="top:0">
      <h2 class="event-name">Harrow<br>Day</h2>
      <p class="event-date">29th<br>October<br>2011</p>
      <ul class="event-details">
        <li>Champagne breakfast from 9am</li>
        <li>Buses to and from the track</li>
        <li>$15 bus ticket includes redeemable drink voucher</li>
        <li>DJ from 8pm until 3am</li>
      </ul>
    </article>
    <article class="event" style="top:102px">
      <h2 class="event-name">Kestrel<br>Plate Eve</h2>
      <p class="event-date">31st<br>October<br>2011</p>
      <ul class="event-details">
        <li>Drink specials all night</li>
        <li>DJ from 8pm until close</li>
      </ul>
    </article>
    <article class="event" style="top:204px">
      <h2 class="event-name">Kestrel<br>Plate Day</h2>
      <p class="event-date">1st<br>November<br>2011</p>
      <ul class="event-details">
        <li>Champagne breakfast from 9am</li>
        <li>Big screen racing live on 3 screens</li>
        <li>Cocktail and drinks specials all day</li>
        <li>DJ from 4pm</li>
      </ul>
    </article>
    <article class="event" style="top:306px">
      <h2 class="event-name">Willows<br>Day</h2>
      <p class="event-date">3rd<br>November<br>2011</p>
      <ul class="event-details">
        <li>Champagne breakfast from 9am</li>
        <li>Buses to and from the track</li>
        <li>$15 bus ticket includes redeemable drink voucher</li>
        <li>DJ from 8pm until close</li>
      </ul>
    </article>
    <article class="event" style="top:408px">
      <h2 class="event-name">Lantern<br>Day</h2>
      <p class="event-date">5th<br>November<br>2011</p>
      <ul class="event-details">
        <li>The finishing post - Complimentary glass of sparkling</li>
        <li>with presentation of race entry ticket</li>
        <li>DJ's from 9pm until 3am</li>
      </ul>
    </article>
  </section>

  <p class="contact-band"><span class="tick" role="img" aria-label="Decorative flourish"></span>FOR FURTHER ENQUIRIES AND TO SECURE YOUR BUS TICKETS PLEASE CONTACT ORLA ON 95184726<span class="tick" role="img" aria-label="Decorative flourish"></span></p>

  <footer class="footer">
    <span class="brand">MAPLE</span>
    <span class="divider divider--one"></span>
    <ul class="address">
      <li>118 Pemberton Street</li>
      <li>West Fairhaven Vic 3917</li>
      <li>West Fairhaven Vic 3917</li>
    </ul>
    <span class="divider divider--two"></span>
    <ul class="social">
      <li><span class="dot"></span>Maple Bar and Restaurant</li>
      <li><span class="dot"></span>@themaplelounge</li>
      <li><span class="dot"></span>maplelounge.example.au</li>
    </ul>
  </footer>
</main>
</body>
</html>
```